VornaDesk website (https://vornadesk.example) re-design

Website purposed for providing general information on products we develop and offer. Products are software specific to online poker players.
Software not playful but complex technological solutions so website should look neatly and professional.
More details on the project you may find in this document:
https://papers.quillnest.example/doc/7TmR2kZpW9xLqB4nVc8YdHs3EfGaJu6KoPi1NwXe/edit#section=s.qkmz4f81b2rn
Or below:
Technology: preferable bootstrap, but not critical
CrossPlatform: Desktop/Mobile
Pages:
Main (Current https://vornadesk.example/)
Video, Room list, Features, Price, Contacts
Partner section (whom we work with)
Documentation and FAQ links
Login (Current https://vornadesk.example/Login/Login)
SignUp/Password recovery (https://vornadesk.example/Signup/Signup, https://vornadesk.example/Login/RemindPassword)
License token (unique and assigned per customer). Need an option to copy to clipboard from Dashboard screen.
Download link for latest product version.
Subs end date to display
Manuals FAQ links
Buy and renew subscription
Notes: Group everything related to subscription into one logic block on the screen.
FAQ (https://vornadesk.example/Home/FAQ).
Simple and comfortable in usage faq.
Notes: Combine all the steps into one screen.
Make download trial which leads to registration!
Target Market(s)
Online poker players
Number of Pages Required
5+ page

```html
<!DOCTYPE html>
<html lang="en">
<head>
<meta charset="utf-8">
<title>VornaDesk</title>
<link href="https://fonts.googleapis.com/css2?family=Poppins:wght@300;400;500;600;700;800&display=swap" rel="stylesheet">
<style>
:root{
  --blue:#2e94d6;
  --blue-deep:#1d6db0;
  --tab:#3b8fd0;
  --ink:#222;
  --text:#777;
  --muted:#999;
  --light:#f5f5f7;
  --footer:#2b2b2b;
  --white:#fff;
}
*{box-sizing:border-box;margin:0;padding:0}
html,body{width:1200px;height:3990px;overflow:hidden}
body{font-family:'Poppins',sans-serif;color:var(--text);background:var(--white);position:relative}
.abs{position:absolute}
.center{text-align:center}

/* header */
.site-header{position:absolute;left:0;top:0;width:1200px;height:98px}
.brand{position:absolute;left:137px;top:28px;font-size:36px;font-weight:600;color:var(--blue);letter-spacing:-.5px}
.nav{position:absolute;right:140px;top:40px;display:flex;gap:26px;font-size:12px;color:#444}
.nav .active{color:var(--blue);border-bottom:2px solid var(--blue);padding-bottom:6px}

/* hero */
.hero{position:absolute;left:74px;top:99px;width:1049px;height:573px;background:linear-gradient(180deg,#c6c6c6 0%,#dedede 55%,#f0f0f0 100%)}
.hero-welcome{position:absolute;top:140px;width:100%;font-size:30px;font-weight:400;color:#333}
.hero-title{position:absolute;top:172px;width:100%;font-size:78px;font-weight:700;color:#222;letter-spacing:-1px;line-height:100px}
.hero-text{position:absolute;top:282px;left:259px;width:531px;font-size:11.5px;line-height:22px;color:#555}
.btn{position:absolute;left:456px;top:371px;width:139px;height:44px;background:var(--blue);color:#fff;font-size:14px;line-height:44px;text-align:center}
.dots{position:absolute;display:flex;gap:6px;align-items:center}
.dots i{width:6px;height:6px;border-radius:50%;background:#aaa;display:block}
.dots i.on{width:8px;height:8px;background:#444}

/* about */
.about{position:absolute;left:0;top:672px;width:1200px;height:438px;background:#fff}
.section-title{position:absolute;width:100%;text-align:center;font-size:58px;font-weight:700;color:var(--ink);letter-spacing:-.5px}
.about p{position:absolute;left:282px;top:190px;width:636px;font-size:11.5px;line-height:22.5px;text-align:center}

/* rooms */
.rooms{position:absolute;left:0;top:1110px;width:1200px;height:971px;background:linear-gradient(160deg,#1c66aa 0%,#2b83c8 50%,#3d93d4 100%)}
.rooms .section-title{color:#fff;top:115px}
.rooms .lead{position:absolute;top:218px;width:100%;text-align:center;font-size:11.5px;line-height:23px;color:#e3efff}
.faq-panel{position:absolute;left:138px;top:311px;width:922px;height:530px;background:#fff}
.faq-tabs{position:absolute;left:0;top:0;width:359px;height:530px;background:var(--tab)}
.tab{display:flex;align-items:center;justify-content:center;text-align:center;color:#fff;font-size:15.5px;font-weight:500;padding:0 40px;line-height:19px;border-top:1px solid rgba(255,255,255,.5)}
.tab.on{background:#fff;color:var(--blue);font-weight:400;border-top:none}
.faq-body{position:absolute;left:436px;top:52px;width:440px}
.faq-body h3{font-size:28px;font-weight:400;color:var(--blue);line-height:34px}
.faq-body p{margin-top:26px;font-size:11.5px;line-height:22.5px;color:#777;width:400px}

/* pricing */
.pricing{position:absolute;left:0;top:2081px;width:1200px;height:582px;background:#fff}
.pricing .section-title{top:80px}
.price-card{position:absolute;top:236px;height:203px;background:#fff;box-shadow:0 4px 22px rgba(0,0,0,.08);padding:38px 40px 0}
.price-card h4{font-size:16px;font-weight:500;color:var(--blue)}
.price-card p{margin-top:12px;font-size:11.5px;line-height:22.5px;color:#777}
.fade-l{position:absolute;left:0;top:220px;width:80px;height:240px;background:linear-gradient(90deg,#fff,rgba(255,255,255,0))}
.fade-r{position:absolute;right:0;top:220px;width:80px;height:240px;background:linear-gradient(270deg,#fff,rgba(255,255,255,0))}
.dots.blue i{background:#9cc7ea}
.dots.blue i.on{background:var(--blue)}

/* partners */
.partners{position:absolute;left:0;top:2663px;width:1200px;height:1140px;background:var(--light)}
.partners .section-title{top:100px}
.partners .lead{position:absolute;top:200px;left:360px;width:480px;text-align:center;font-size:11.5px;line-height:22.5px}
.partner{position:absolute;width:200px;text-align:center}
.partner .mark{width:110px;height:110px;border-radius:18px;margin:0 auto}
.partner .name{margin-top:28px;font-size:17px;font-weight:500;color:#333;line-height:19px}
.divider{position:absolute;width:1px;height:150px;background:#ddd}

/* footer */
.site-footer{position:absolute;left:0;top:3803px;width:1200px;height:187px;background:var(--footer);color:#fff}
.site-footer .brand{top:55px}
.foot-info{position:absolute;left:137px;top:120px;display:flex;align-items:center;font-size:11.5px}
.foot-info .sep{width:1px;height:28px;background:#888;margin:0 18px}
.copy{position:absolute;right:140px;top:120px;font-size:11.5px}
.social{position:absolute;right:140px;top:66px;display:flex;gap:12px}
.social i{width:27px;height:27px;border-radius:50%;background:#fff;display:block}
</style>
</head>
<body>

<header class="site-header">
  <div class="brand">VornaDesk</div>
  <nav class="nav">
    <span class="active">Home</span><span>My Subscriptions</span><span>FAQ's</span><span>Contact Us</span>
  </nav>
</header>

<section class="hero" role="img" aria-label="Light grey hexagon texture backdrop">
  <div class="hero-welcome center">Welcome To</div>
  <div class="hero-title center">VornaDesk</div>
  <p class="hero-text center">Lorem Ipsum Is Simply Dummy Text Of The Printing And Typesetting Industry. Lorem Ipsum<br>Has Been The Industry's Standard Dummy Text Ever Since The 1500s,</p>
  <div class="btn">Learn More</div>
  <div class="dots" style="left:504px;top:527px"><i></i><i class="on"></i><i></i><i></i></div>
</section>

<section class="about">
  <h2 class="section-title" style="top:80px">About Us</h2>
  <p>Lorem Ipsum Is Simply Dummy Text Of The Printing And Typesetting Industry. Lorem Ipsum Has Been The Industry's Standard Dummy Text Ever Since The 1500s, When An Unknown Printer Took A Galley Of Type And Scrambled It To Make A Type Specimen Book.<br>It Has Survived Not Only Five Centuries, But Also The Leap Into Electronic Typesetting, Remaining Essentially Unchanged. It Was Popularised In The 1960s With The Release Of Sheetmark Sheets Containing Lorem Ipsum Passages, And More Recently With Desktop Publishing Software Like Quillset Layout Including Versions Of Lorem Ipsum.</p>
</section>

<section class="rooms" role="img" aria-label="Blue tinted photo of a poker player at a table">
  <h2 class="section-title">Rooms &amp; Features</h2>
  <p class="lead">Lorem Ipsum Is Simply Dummy Text Of The Printing And Typesetting Industry.<br>Lorem Ipsum Has Been The Industry's Standard Dummy Text Ever</p>
  <div class="faq-panel">
    <div class="faq-tabs">
      <div class="tab on" style="height:85px">Which Rooms Does VornaDesk Support?</div>
      <div class="tab" style="height:71px">Can't Find Your Room In The List?</div>
      <div class="tab" style="height:68px">Does VornaDesk Working With VPN?</div>
      <div class="tab" style="height:91px">How Many Tables I May Play At The Same Time With VornaDesk Running?</div>
      <div class="tab" style="height:71px">Does Pipcard Support 5 Card PLO?</div>
      <div class="tab" style="height:70px">Do You Support ShortDeck Play?</div>
      <div class="tab" style="height:74px">Does VornaDesk Support Tourneys?</div>
    </div>
    <div class="faq-body">
      <h3>Which Rooms Does VornaDesk Support?</h3>
      <p>TableLedger 2: Support For TL2 (Default). Shows HUD Based On Converted Hands.<br>HandScope 4: Support For HS4. Shows HUD Based On Converted Hands. "HS4" Checkbox Must Be Selected On Converter Window.<br>QTR API: Supports QTR Natively Through API. No Additional Configuration. Shows QTR HUD. Please Note, You Must Have QTR "Asia" Add-On Subscription.<br>Free Seat Alert: Alerts When Free Seat Available On Earlier Full Table.<br>Mobile Emulator: Mobile Emulator Supported.<br>Mobile VPN: If Using Mobile VPN Supported.<br>Full Stack, Kestrel, Chiptime, Yourdeal &amp; Ourtable While Playing With QTR Write Hands Into Stackvault Database.</p>
    </div>
  </div>
</section>

<section class="pricing">
  <h2 class="section-title">Pricing &amp; Purchasing</h2>
  <div class="price-card" style="left:-190px;width:500px">
    <h4 style="padding-left:190px">The Refund Policy?</h4>
    <p style="padding-left:190px">If Stable With No Issues We Do 50% Which Is Used Less Or Equal To 14 Days. Refund Is Not Supposed If Operational Or Does Not Work.</p>
  </div>
  <div class="price-card center" style="left:347px;width:504px">
    <h4>Do You Have Discounts Or Promotions?</h4>
    <p>With 3 Months Purchase We Provide 10% Discount<br>And With 6 Months Subscription 20% Discount Is<br>Applied</p>
  </div>
  <div class="price-card" style="left:889px;width:500px;padding-left:80px">
    <h4 style="white-space:nowrap">What Is The Price For</h4>
    <p style="white-space:nowrap">Price Depends On Stakes<br>Plan B, Any Stakes, All<br>Plan A, Stakes 2/4/8 And Up<br>Note: There Is No Low Stakes Plan</p>
  </div>
  <div class="fade-l"></div><div class="fade-r"></div>
  <svg class="abs" style="left:493px;top:473px" width="62" height="12" viewBox="0 0 62 12"><path d="M61 6H2M7 1L1 6l6 5" stroke="#2e94d6" stroke-width="1.5" fill="none"/></svg>
  <div class="dots blue" style="left:578px;top:476px"><i></i><i class="on"></i><i></i><i></i></div>
  <svg class="abs" style="left:645px;top:473px" width="62" height="12" viewBox="0 0 62 12"><path d="M1 6h59M55 1l6 5-6 5" stroke="#2e94d6" stroke-width="1.5" fill="none"/></svg>
</section>

<section class="partners">
  <h2 class="section-title">Whom We Work With</h2>
  <p class="lead">Lorem Ipsum Is Simply Dummy Text Of The Printing And Typesetting Industry. Lorem Ipsum Has Been The Industry's Standard Dummy Text Ever Since The 1500s, When An Unknown Printer Took A Galley Of Type And Scrambled It To Make A Type Specimen Book.</p>

  <div class="divider" style="left:293px;top:345px"></div>
  <div class="divider" style="left:495px;top:345px"></div>
  <div class="divider" style="left:700px;top:345px"></div>
  <div class="divider" style="left:904px;top:345px"></div>
  <div class="divider" style="left:293px;top:595px"></div>
  <div class="divider" style="left:495px;top:595px"></div>
  <div class="divider" style="left:700px;top:595px"></div>
  <div class="divider" style="left:904px;top:595px"></div>
  <div class="divider" style="left:599px;top:852px"></div>

  <div class="partner" style="left:92px;top:365px"><div class="mark" style="background:#2a1414"></div><div class="name">Crimson Kite<br>Poker</div></div>
  <div class="partner" style="left:295px;top:365px"><div class="mark" style="background:#22c3a9"></div><div class="name">Ourtable</div></div>
  <div class="partner" style="left:499px;top:365px"><div class="mark" style="background:#141414;border-radius:2px"></div><div class="name">Crown Felt<br>Asia</div></div>
  <div class="partner" style="left:703px;top:365px"><div class="mark" style="background:#111"></div><div class="name">Yourdeal</div></div>
  <div class="partner" style="left:906px;top:365px"><div class="mark" style="background:#f4a40c"></div><div class="name">Felt<br>Circle</div></div>

  <div class="partner" style="left:92px;top:616px"><div class="mark" style="background:#121212;border-radius:2px"></div><div class="name">Deckwise</div></div>
  <div class="partner" style="left:295px;top:616px"><div class="mark" style="background:#173322;border-radius:2px"></div><div class="name">Pipcard/Duo<br>Poker</div></div>
  <div class="partner" style="left:499px;top:616px"><div class="mark" style="background:#2d2d2d"></div><div class="name">Truehand</div></div>
  <div class="partner" style="left:703px;top:616px"><div class="mark" style="background:#1aa188;border-radius:2px"></div><div class="name">Chiptime</div></div>
  <div class="partner" style="left:906px;top:616px"><div class="mark" style="background:#b8272c;border-radius:2px"></div><div class="name">Full Stack</div></div>

  <div class="partner" style="left:397px;top:873px"><div class="mark" style="background:#111"></div><div class="name">Minnow Poker</div></div>
  <div class="partner" style="left:601px;top:873px"><div class="mark" style="background:#151515"></div><div class="name">Lotto (Ex Brew<br>Tea)</div></div>
</section>

<footer class="site-footer">
  <div class="brand">VornaDesk</div>
  <div class="social"><i></i><i></i><i></i></div>
  <div class="foot-info"><span>Support: help@vornadesk.example</span><span class="sep"></span><span>Wirechat Official Channel: wire.example/vornadesk</span></div>
  <div class="copy">© 2019 VornaDesk. All Right Reserved</div>
</footer>

</body>
</html>
```